Lens Harbor Teutonia Website - Photography and Films

We are looking for a design that expresses the friendly, open nature of our company Lens Harbor Teutonia, yet at the same time is professional looking and functional.

Lens Harbor Teutonia is a B2B focused operation that hires out multi-lingual camera crews (and equipment) throughout Germany and Europe. We also produce tv features and coporate films. Our unique selling point is that we are native English speakers who can communicate with our international clients (usually British or American) and organise the logistics of shooting in foreign countries.

For content inspiration, see our current website: http://www.lensharborteutonia.com - however we want to move away from the very simple structure of this site and move towards a layout that displays and allows for frequently updated content (e.g. in the form of a blog).

Here is an example of the kind of clean look we like:
http://www.qrvpixelarchive.com/archive/main/reelsqrv.do#reel=48213760

Please keep within the following specifications:
- We wish to keep our logo (grey/white, font: Glypha) and our company colour red (#C40A0A) as they are.
- Maximum Width 960px, on a large browser-window the design should be centred
- Easily readable font sizes with good contrast
- Provide your design in PSD file format
- Our logo should be graphically displayed in the top left of the header.
- The design should allow space for a video.
- The page should have a clearly recognisable end in the form of a footer.

The following menu items need to be clearly arranged so the viewer is not overwhelmed or confused:
About
Services - Crews / Corporate Shoots / Webcasts / Production Arm / Legal Videography
Recent Productions
Blog
Testimonials
Get a Quote
Contact
Film Library
Showreel
Events
Film Location Guide - Frankfurt / Cologne / Zurich / Helsinki / Amsterdam / London / Paris / Rome / Brussels / Berlin / Munich
Updates

Reason: Hi - thanks very much for your interest in our design project.  We are extending this auction because we haven't had enough time to really focus on the desigs and provide immediate feedback to designers.  We will try to provide timely feedback and are giving you more time to make any adjustments to your designs etc.
Thanks!
Marla

Target Market(s)

Our target customers are males and females between 25 and 55 years (mostly British and American). More important than their demographic though, is their occupation - they are largely communication and design savvy individuals belonging to one of the following three categories: 1)Broadcasters (usually producers for example from the QRV or Horizon Vista TV seeking trustworthy, affordable crews for their foreign shoots).

2) Video Production Companies (seeking a trustworthy, affordable partner company to provide the crews for their own corporate clients).

3) Corporate Communications Specialists (seeking professional producers and crews to facilitate production of company videos or filming of events).

Industry/Entity Type

Camera

Requirements
Must have
• A fresh clean appearance with good use of white space.
Should not have
• Avoid dark heavy colours and designs.
• Avoid designs that would be impractical and could potentially take a long time to load.

```html
<!DOCTYPE html>
<html lang="en">
<head>
<meta charset="utf-8">
<title>Lens Harbor Teutonia</title>
<link href="https://fonts.googleapis.com/css2?family=Open+Sans:wght@400;700;800&display=swap" rel="stylesheet">
<style>
  :root {
    --brand-red: #a50c0c;
    --brand-red-dark: #9a0a0a;
    --panel-grey: #bfc0c6;
    --page-white: #ffffff;
    --ink: #1f1f1f;
    --photo-light: #b9b6b0;
    --photo-dark: #3a3a3a;
  }
  * { margin: 0; padding: 0; box-sizing: border-box; }
  html, body { width: 1125px; height: 1200px; overflow: hidden; }
  body {
    background: repeating-linear-gradient(180deg, var(--brand-red) 0 5px, var(--brand-red-dark) 5px 6px);
    font-family: "Open Sans", sans-serif;
  }
  .page {
    position: absolute; left: 0; top: 0;
    width: 960px; height: 1024px;
    transform: scale(1.171875); transform-origin: 0 0;
  }
  .sheet { position: absolute; left: 100px; top: 0; width: 760px; height: 1024px; background: var(--page-white); }
  .masthead { position: absolute; left: 100px; top: 0; width: 760px; height: 77px; background: var(--brand-red); }
  .logo {
    position: absolute; left: 128px; top: 22px;
    font-weight: 800; font-size: 23px; color: #fff; letter-spacing: -0.3px;
  }
  .main-nav {
    position: absolute; left: 297px; top: 62px; width: 663px; height: 29px;
    background: var(--panel-grey); border-radius: 15px 0 0 15px;
    display: flex; align-items: center; padding-left: 122px;
    font-size: 17px; color: #fff;
  }
  .main-nav span { white-space: pre; }
  .services-menu {
    position: absolute; left: 445px; top: 106px; width: 115px; height: 110px;
    background: var(--panel-grey); border-radius: 8px 0 8px 8px;
  }
  .services-tab { position: absolute; left: 503px; top: 91px; width: 57px; height: 20px; background: var(--panel-grey); }
  .caret { position: absolute; left: 527px; top: 85px; width: 0; height: 0;
    border-left: 3px solid transparent; border-right: 3px solid transparent; border-top: 4px solid #fff; }
  .submenu-list { list-style: none; text-align: right; color: #fff; font-size: 12px; line-height: 16.5px; }
  .services-menu .submenu-list { padding: 13px 8px 0 0; }
  .crew-photo {
    position: absolute; left: 102px; top: 102px; width: 241px; height: 412px;
    border-radius: 8px;
    background: linear-gradient(160deg, #8a8c8e 0%, var(--photo-dark) 35%, #2b2b2b 60%, var(--photo-light) 100%);
  }
  .side-nav {
    position: absolute; left: 0; top: 536px; width: 346px; height: 168px;
    background: var(--panel-grey); border-radius: 0 8px 0 0;
  }
  .side-nav ul { list-style: none; text-align: right; color: #fff; font-size: 19.5px; line-height: 26px; padding: 12px 26px 0 0; }
  .location-menu {
    position: absolute; left: 253px; top: 692px; width: 92px; height: 209px;
    background: var(--panel-grey); border-radius: 8px 0 8px 8px;
  }
  .location-menu .submenu-list { padding: 21px 14px 0 0; line-height: 16.3px; }
  .location-notch { position: absolute; left: 253px; top: 692px; width: 34px; height: 12px; background: var(--page-white); }
  .headline {
    position: absolute; left: 380px; top: 530px; width: 442px;
    text-align: center; font-weight: 400; font-size: 28px; line-height: 34px; color: var(--ink);
  }
  .intro {
    position: absolute; left: 393px; top: 630px; width: 445px;
    font-size: 12.2px; line-height: 16.3px; color: var(--ink);
  }
  .intro p + p { margin-top: 16.3px; }
  .features { list-style: none; margin: 16.3px 0 0 12px; }
  .features li { padding-left: 10px; text-indent: -10px; }
  .site-footer {
    position: absolute; left: 100px; top: 985px; width: 760px; height: 39px;
    background: var(--brand-red); color: #fff; text-align: center;
    font-size: 11px; line-height: 16px; padding-top: 4px;
  }
</style>
</head>
<body>
<div class="page">
  <div class="sheet"></div>
  <header class="masthead"></header>
  <div class="logo">lensharborteutonia</div>
  <nav class="main-nav">
    <span>About   |   Services   |   Blog   |   Film Library   |   contact</span>
  </nav>
  <span class="caret"></span>
  <div class="services-tab"></div>
  <div class="services-menu">
    <ul class="submenu-list" style="margin-top:-11px">
      <li>Crews</li><li>Corporate Shots</li><li>Webcasts</li><li>production Arm</li><li>Legal Videography</li>
    </ul>
  </div>

  <div class="crew-photo" role="img" aria-label="Camera operator with a video camera on a tripod at an outdoor location"></div>

  <nav class="side-nav">
    <ul>
      <li>Recent Productions</li><li>Testimonials</li><li>Get a Quote</li><li>Events</li><li>Film Location Guide ▾</li>
    </ul>
  </nav>
  <div class="location-menu">
    <ul class="submenu-list">
      <li>Frankfurt</li><li>Cologne</li><li>Zurich</li><li>Helsinki</li><li>Amsterdam</li><li>London</li><li>Paris</li><li>Rome</li><li>Brussels</li><li>Berlin</li><li>Munich</li>
    </ul>
  </div>

  <h1 class="headline">english speaking camera crews throughout germany and europe</h1>

  <section class="intro">
    <p>We set up Lens Harbor Teutonia to meet the demands of a growing number of TV-producers whose working language is English. This is our Passion! Why else would we keep doing it for over 30 years!<br>
    As a producer, you’re bound to have great ideas…but how do you make them a reality in a country where you can’t speak the language? Partner with us! We are native English speakers so nothing gets lost in translation. We’ll catch hold of your vision, and with local know-how, we’ll make it happen.</p>
    <p>No job is too big, too small, too hard, too far away, or too urgent. Try us!</p>
    <ul class="features">
      <li>* We provide camera crews and facilities throughout Germany and Europe</li>
      <li>* We shoot in both PAL and NTSC</li>
      <li>* We edit either in-studio or on the move and we transfer urgent footage via FTP or SNG</li>
      <li>* We are on call 24/7</li>
    </ul>
    <p style="margin-top:16.3px">To make a no obligation enquiry about any of our services, please call our Frankfurt Headquarters: +49-69-555014 (Toll free from the USA 1-866-555-0142) or click here to get a quote.</p>
  </section>

  <footer class="site-footer">
    c/o Brannock Films • Lindenweg 12 • 60311 Frankfurt/Main • Germany • info@lens-harbor-teutonia.com<br>
    Tel.: +49-69-555014 • Toll free from the USA 1-866-555-0142
  </footer>
</div>
</body>
</html>
```